Website: Orvalink Business Consultants, Qianhai SEZ, China

Our client is a business consultancy firm and will be the first to set up in the Qianhai Shenzhen-Hong Kong Modern Service Industry Cooperation Zone, China So we need a corporate website concept that engages service, finance and technology sector companies. The company can provide all the necessary services needed to set up shop in Qianhai. They are looking for a modern, international, reliable and strong image.

Here are some websites for reference prupose:

http://www.brenwickpartners.example/ (we like the dynamic banner and clear, clean layout of this website)

http://www.dovetrassadvisory.example/ (we like the background city image, use of light font, hover over menu functions and color scheme - purple and grey)

http://www.pelmo.example/ (we like the simplicity of this website, clear lines and we like the dynamic banner)
Updates

Hello, We are currently undecided between three logo designs.  All three have been uploaded to the design brief so that you can use them as reference for the website design. Thx

Also please take note of the addition menu selection 'About Qianhai'. Thx

Hello all Designers, First of all we want thank you for participating in our website competition, the calibre of design was high and we appreciated the expedience. Our company is Quillon Reach Web Design and Internet Marketing based in Shenzhen, China. We anticipate rapid growth in the Chinese domestic market as the country shifts in to a service sector economy. We hope to continue building reliable working relationships with you based on idea sharing and constructive feedback. Once again, Thankyou, QR Team

Target Market(s)

International finance and technology companies looking to set up in Qianhai Special Economic Zone, China

Industry/Entity Type

Finance

Requirements
Must have
• Initial design for home page and in later selection stages a secondary page will be required.

The design should be for PSD concepts only no code!

Menu bar, Photo banner -
A. Photo banner and text overlay,
B.Photo Banner and text description to left or right.

Social Connect icons, Site search bar (top right), Logo space (top left).

Menu bar at top with Home, About Us, About Qianhai, Services, Portfolio, Partners, Our Team Contact Us.

Standard 3-4 box layout - Banner at top and 2-3 boxes under banner.

Colour scheme- A. Purple and Blue, must have light background/body
B. Shades of white, black and grey.

Simple, clear, clean, sharp.

```html
<!DOCTYPE html>
<html lang="en">
<head>
<meta charset="utf-8">
<title>Orvalink Business Consulting</title>
<link href="https://fonts.googleapis.com/css2?family=Arimo:wght@400;700&display=swap" rel="stylesheet">
<style>
:root{
  --bar-top:#4a4a4a;
  --bar-bottom:#1c1c1c;
  --green:#9db24d;
  --green-soft:#b5c76a;
  --link-green:#8fa63a;
  --ink:#222;
  --body:#7a7a7a;
  --line:#dcdcdc;
  --strip-1:#333;
  --strip-2:#666;
  --strip-3:#dedede;
}
*{margin:0;padding:0;box-sizing:border-box}
html,body{width:1200px;height:1045px;overflow:hidden;background:#fff}
body{font-family:"Arimo",Arial,sans-serif;color:var(--ink)}
.stage{position:absolute;left:0;top:0;width:1490px;height:1298px;transform:scale(0.80537);transform-origin:0 0;overflow:hidden}
.abs{position:absolute}

.topbar{left:0;top:0;width:1490px;height:66px;background:linear-gradient(var(--bar-top),var(--bar-bottom))}
.nav{left:233px;top:0;height:66px;display:flex;list-style:none}
.nav li{height:66px;line-height:72px;font-size:14px;color:#fff;padding:0 13px;position:relative;white-space:nowrap}
.nav li.active{background:linear-gradient(#151515,#2b2b2b);padding:0 25px 0 24px}
.nav li.active::after{content:"";position:absolute;left:50%;bottom:0;margin-left:-6px;border:6px solid transparent;border-bottom:8px solid #fff;border-top:0}
.search{left:988px;top:16px;width:235px;height:32px;background:linear-gradient(#fff,#e6e6e6);border:1px solid #999;border-radius:2px;font-size:12px;color:#666;padding:12px 0 0 9px}
.search-icon{left:1231px;top:20px}

.brand{left:234px;top:82px;display:flex;align-items:flex-end;gap:10px}
.brand-mark{width:40px;height:40px;border-radius:50%;background:#444;margin-bottom:8px}
.brand-name{font-size:19px;color:#444;letter-spacing:0.5px;line-height:1}
.brand-sub{font-size:7px;letter-spacing:3.4px;color:#555;margin-top:4px}

.social{left:1143px;top:119px;display:flex;gap:4px}
.social span{width:35px;height:35px;background:#2b2b2b}

.banner{left:230px;top:188px;width:1028px;height:358px}
.strip{top:0;height:358px}
.s1{left:0;width:43px;background:var(--strip-1)}
.s2{left:43px;width:43px;background:var(--strip-2)}
.s3{left:86px;width:41px;background:var(--strip-3)}
.pager{top:324px;width:23px;height:23px;border-radius:50%;background:var(--green-soft)}
.pager svg{display:block}
.panel{left:127px;top:0;width:310px;height:358px;background:var(--green);color:#fff}
.panel h1{position:absolute;left:27px;top:44px;font-size:24px;font-weight:400;line-height:28px;width:240px}
.panel p{position:absolute;left:27px;top:146px;width:256px;font-size:12px;line-height:18px;letter-spacing:0.2px}
.btn{position:absolute;left:29px;top:252px;width:104px;height:32px;border:2px solid #cfd9a3;background:linear-gradient(#fff,#e4e4e4);color:#444;font-size:12px;text-align:center;line-height:28px}
.slide-no{position:absolute;left:278px;top:328px;width:24px;height:24px;border-radius:50%;background:#000;font-size:12px;font-weight:700;text-align:center;line-height:24px}
.photo{left:437px;top:0;width:591px;height:358px;background:linear-gradient(100deg,#f8f8f8 0%,#e2e2e2 35%,#9a9a9a 70%,#3e3e3e 100%)}

h2{font-size:18px;font-weight:400;color:var(--ink)}
.rule{height:1px;background:var(--line)}
.left-col{left:234px;top:577px;width:314px}
.partners{display:grid;grid-template-columns:1fr 1fr;row-gap:24px;padding:12px 0 14px}
.partner{display:flex;align-items:center;gap:8px;font-size:20px;color:#555;height:36px}
.partner i{width:30px;height:22px;background:#666;display:block}
.partner.r{justify-content:flex-end}
.dots{display:flex;gap:8px}
.dots span{width:9px;height:9px;border-radius:50%;background:#aaa}
.dots span.on{background:var(--green)}
.quote{left:233px;top:846px;width:305px;height:84px;border:1px solid #ddd;box-shadow:1px 1px 2px #eee;font-size:12px;line-height:18px;color:#888;padding:13px 8px 0 33px;letter-spacing:0}
.qmark{font-size:30px;color:#ddd;font-family:Georgia,serif}
.qmark.open{position:absolute;left:10px;top:2px}
.qmark.close{font-size:24px;line-height:0;vertical-align:-9px;margin-left:4px}
.avatar{left:234px;top:971px;width:73px;height:46px;border:1px solid #ddd;padding:3px}
.avatar div{width:100%;height:100%;background:linear-gradient(120deg,#3b4b63,#b3a18e)}
.contact-ico{width:36px;height:36px;border:1px solid #ccc;background:linear-gradient(#fff,#e5e5e5)}
.contact-label{font-size:12px;color:#333}
.contact-val{font-size:15px;color:var(--link-green)}

.vline{left:579px;top:577px;width:1px;height:577px;background:var(--line)}
.right-col{left:614px;width:646px}
.sub{font-size:12px;color:#333;text-decoration:underline}
.copy{font-size:12px;line-height:18px;color:var(--body);letter-spacing:0.3px}
.more{display:inline-flex;align-items:center;gap:8px;font-size:11px;color:var(--link-green);text-decoration:underline;letter-spacing:0}
.more i{display:inline-block;width:16px;height:10px;background:var(--green)}
.hr-soft{left:614px;top:874px;width:644px;height:1px;background:linear-gradient(90deg,#fff,#ddd 40%,#ddd 60%,#fff)}
.svc{width:310px}

.footer{left:233px;top:1193px;width:1024px;height:58px;border-top:1px solid #ddd;border-bottom:1px solid #ddd;background:linear-gradient(#fff,#f6f6f6);font-size:12px;color:#888}
.footer .links{position:absolute;left:21px;top:23px}
.footer .links b{font-weight:400;color:#bbb;margin:0 6px}
.footer .legal{position:absolute;right:24px;top:23px}
.footer .legal span{color:#111}
</style>
</head>
<body>
<div class="stage">

  <header>
    <div class="abs topbar"></div>
    <ul class="abs nav">
      <li class="active">Home</li><li>About Us</li><li>About Qianhai</li><li>Services</li><li>Portfolio</li><li>Partners</li><li>Our Team</li><li>Contact Us</li>
    </ul>
    <div class="abs search">Search...</div>
    <svg class="abs search-icon" width="26" height="26" viewBox="0 0 26 26"><circle cx="10" cy="10" r="7.5" fill="none" stroke="#fff" stroke-width="2.4"/><line x1="15.5" y1="15.5" x2="24" y2="24" stroke="#fff" stroke-width="3.2" stroke-linecap="round"/></svg>

    <div class="abs brand">
      <div class="brand-mark"></div>
      <div><div class="brand-name">ORVALINK</div><div class="brand-sub">BUSINESS CONSULTING</div></div>
    </div>
    <div class="abs social" aria-label="Social links"><span></span><span></span><span></span></div>
  </header>

  <section class="abs banner">
    <div class="abs strip s1"></div>
    <div class="abs strip s2"></div>
    <div class="abs strip s3"></div>
    <div class="abs pager" style="left:11px"><svg width="23" height="23"><path d="M8 8l7 7M15 10v5h-5" stroke="#fff" stroke-width="2" fill="none"/></svg></div>
    <div class="abs pager" style="left:53px"><svg width="23" height="23"><path d="M8 8l7 7M15 10v5h-5" stroke="#fff" stroke-width="2" fill="none"/></svg></div>
    <div class="abs pager" style="left:96px"><svg width="23" height="23"><path d="M8 8l7 7M15 10v5h-5" stroke="#fff" stroke-width="2" fill="none"/></svg></div>
    <div class="abs panel">
      <h1>Lorem ipsum dolor sit amet, consectetur adipiscing elit.</h1>
      <p>Sed vel erat mi. Nam dignissim adipiscing. Vestibulum varius mollis eleifend. Ut ipsum urna, sollicitudin vitae ultricies nec, dictum vel mauris. Integer elementum mi sit amet lectus varius condimentum.</p>
      <div class="btn">Learn More</div>
      <div class="slide-no">01</div>
    </div>
    <div class="abs photo" role="img" aria-label="Black and white photo of three consultants at a meeting table with a laptop in a bright office"></div>
  </section>

  <aside>
    <div class="abs left-col">
      <h2 style="margin-top:10px">Our Partners</h2>
      <div class="rule" style="margin-top:21px"></div>
      <div class="partners">
        <div class="partner"><i></i>Calderix</div>
        <div class="partner r">Nuvaro</div>
        <div class="partner">Tessly</div>
        <div class="partner r">Brightlume</div>
      </div>
      <div class="rule"></div>
      <div style="display:flex;justify-content:space-between;align-items:center;margin-top:32px;padding-right:12px">
        <h2>Testimonials</h2>
        <div class="dots"><span></span><span class="on"></span><span></span></div>
      </div>
    </div>
    <div class="abs quote">
      <span class="qmark open">&ldquo;</span>Sed sagittis diam eu nunc dapibus vel placerat urna ultrices. Integer dolor nisl, dignissim ut so dales ut, imperdiet condimentum dolor.<span class="qmark close">&rdquo;</span>
    </div>
    <svg class="abs" style="left:270px;top:929px" width="28" height="34"><path d="M1 0L3 33L26 0" fill="#fff" stroke="#ddd"/><rect x="1.5" y="0" width="24" height="1.5" fill="#fff"/></svg>
    <div class="abs avatar"><div role="img" aria-label="Portrait photo of the client"></div></div>
    <div class="abs" style="left:320px;top:977px;font-size:12px;color:#444">R.Kellan.Moss</div>
    <div class="abs copy" style="left:320px;top:995px">Lorem ipsum dolor <span style="color:var(--link-green)">more[...]</span></div>

    <div class="abs rule" style="left:234px;top:1047px;width:314px"></div>
    <div class="abs contact-ico" style="left:236px;top:1059px"><svg width="34" height="34"><path d="M12 8c-3 1-4 4-2 9s6 9 10 9c2 0 3-1 3-2l-3-3-2 1c-2-1-4-4-5-6l1-2-2-6z" fill="#444"/></svg></div>
    <div class="abs contact-label" style="left:284px;top:1061px">Call for consultation</div>
    <div class="abs contact-val" style="left:283px;top:1079px">000-555-014-270</div>
    <div class="abs rule" style="left:234px;top:1106px;width:314px"></div>
    <div class="abs contact-ico" style="left:236px;top:1117px"><svg width="34" height="34"><rect x="6" y="11" width="22" height="13" fill="none" stroke="#444" stroke-width="1.6"/><path d="M6 11l11 8 11-8M6 24l8-6M28 24l-8-6" fill="none" stroke="#444" stroke-width="1.4"/></svg></div>
    <div class="abs contact-label" style="left:284px;top:1119px">Email at</div>
    <div class="abs contact-val" style="left:283px;top:1137px">info@orvalink.example</div>
  </aside>

  <div class="abs vline"></div>

  <main>
    <div class="abs right-col" style="top:587px">
      <h2>About Us</h2>
      <div class="sub" style="margin-top:16px">Lorem ipsum dolor sit amet, consectetur adipiscing elit.&nbsp;</div>
      <p class="copy" style="margin-top:14px">Lorem ipsum dolor sit amet, consectetur adipiscing elit. Nunc rutrum lectus id nibh semper id fermentum neque condimentum. Donec ut nunc mauris, non luctus mauris.</p>
      <p class="copy" style="margin-top:12px">Donec semper purus vitae nunc varius ac ultricies libero lacinia. Phasellus auctor aliquet arcu, sed scelerisque purus hendrerit at. Ut a nisi at mauris laoreet interdum sit amet at mauris. Aliquam quis odio nec erat mollis tempus. In rhoncus ligula ut sapien vestibulum ut vestibulum nisi lobortis. Pellentesque laoreet semper leo, et aliquet nulla dictum sed. Aliquam auctor rhoncus fringilla.</p>
      <p class="copy" style="margin-top:10px">Sed ornare diam vitae orci ultricies ultricies. Nulla molestie orci vel neque ornare tincidunt. Vivamus nec sem lorem. Mauris sit amet tempor dui. Integer consequat pulvinar velit. Nunc vitae urna neque, ut sagittis tortor</p>
      <div class="more" style="margin-top:10px"><i></i>Read More</div>
    </div>
    <div class="abs hr-soft"></div>
    <div class="abs right-col" style="top:897px">
      <h2>Our Services</h2>
      <div style="display:grid;grid-template-columns:338px 310px;row-gap:18px;margin-top:18px">
        <div class="svc"><div class="sub">Lorem ipsum dolor sit amet</div><p class="copy" style="margin-top:14px">Lorem ipsum dolor sit amet, consectetur adipiscing elit. Nunc rutrum lectus id nibh semper id fermentum neque condimentum. Donec ut nunc mauris, non luctus mauris. <span class="more"><i></i>Read More</span></p></div>
        <div class="svc"><div class="sub">Lorem ipsum dolor sit amet</div><p class="copy" style="margin-top:14px">Lorem ipsum dolor sit amet, consectetur adipiscing elit. Nunc rutrum lectus id nibh semper id fermentum neque condimentum. Donec ut nunc mauris, non luctus mauris. <span class="more"><i></i>Read More</span></p></div>
        <div class="svc"><div class="sub">Lorem ipsum dolor sit amet</div><p class="copy" style="margin-top:14px">Lorem ipsum dolor sit amet, consectetur adipiscing elit. Nunc rutrum lectus id nibh semper id fermentum neque condimentum. Donec ut nunc mauris, non luctus mauris. <span class="more"><i></i>Read More</span></p></div>
        <div class="svc"><div class="sub">Lorem ipsum dolor sit amet</div><p class="copy" style="margin-top:14px">Lorem ipsum dolor sit amet, consectetur adipiscing elit. Nunc rutrum lectus id nibh semper id fermentum neque condimentum. Donec ut nunc mauris, non luctus mauris. <span class="more"><i></i>Read More</span></p></div>
      </div>
    </div>
  </main>

  <footer class="abs footer">
    <div class="links">Home<b>|</b>About Us<b>|</b>About Qianhai<b>|</b>Services<b>|</b>Portfolio<b>|</b>Partners<b>|</b>Our Team<b>|</b>Contact Us</div>
    <div class="legal">Copyright © 2013 <span>Orvalink</span>. All rights reserved</div>
  </footer>

</div>
</body>
</html>
```